Service Menu refresh 2018 Update of menu pricing

We currently have service menus as attached. We will be updating our look via our homepage image, our service menu and our in-house beverage and treatment menu.
We are a natural and sustainable hair salon group and moving more towards head spa which consists of treatments, beauty, tanning as well as your traditional hair services. Our imagery needs to reflect our efforts in spa treatments in the hair and scalp area and use natural materials and colours reflecting sustainability.
Velin is the brand we stock and promote.

Target Market(s)

Men or women interesting in personal maintenance with natural and organic products and using sustainable practises

Industry/Entity Type

Hair And Beauty

Font styles to use
Sans Serif
Other font styles liked:
• Arial or Helvetica

Colors
9acb3c
abd037
cadf82
ffffff

Requirements
Must have
• Name on the front cover, locations on back cover
Nice to have
• Prestige feel, reflect male and female clients
Should not have
• Bold artificial writing or any type of cartoon images.
• Same images as existing menu.

```html
<!DOCTYPE html>
<html lang="en">
<head>
<meta charset="utf-8">
<title>Verdant Roots – Service Menu</title>
<link href="https://fonts.googleapis.com/css2?family=Arimo:wght@400;700&family=Roboto+Condensed:wght@400;700&family=EB+Garamond:ital@1&display=swap" rel="stylesheet">
<style>
:root{
  --bg:#acd23c;
  --green:#9acb3c;
  --green-text:#8cc63f;
  --pale:#cadf82;
  --white:#ffffff;
  --ink:#1d1d1b;
  --black:#0d0d0d;
}
*{margin:0;padding:0;box-sizing:border-box}
html,body{width:1200px;height:1200px;overflow:hidden}
body{background:var(--bg);position:relative;font-family:"Arimo",Arial,sans-serif;color:var(--ink)}
.sheet{position:absolute;left:100px;width:1000px;background:var(--white);box-shadow:0 8px 14px rgba(60,90,0,.25)}
.cover{top:50px;height:500px}
.menu{top:602px;height:546px}

/* cover: back side with locations */
.quote{position:absolute;left:60px;top:26px;width:440px;font-family:"EB Garamond",Georgia,serif;font-style:italic;font-size:23px;line-height:29px;color:#2a2a2a;text-align:center}
.quote .mark{color:var(--green);font-size:34px;font-weight:700;line-height:0;vertical-align:-2px}
.quote-rule{position:absolute;left:132px;top:92px;width:236px;height:2px;background:var(--green)}
.locations{position:absolute;left:22px;top:100px;font-size:12.6px;line-height:16.8px}
.location{margin-bottom:4.3px}
.location h3{color:var(--green-text);font-size:13px;font-weight:700;letter-spacing:.1px}
.web-bar{position:absolute;left:0;top:459px;width:415px;height:29px;background:linear-gradient(90deg,var(--black) 82%,rgba(13,13,13,0));color:var(--green-text);font-weight:700;font-size:13px;line-height:29px;padding-left:128px;letter-spacing:.2px}

/* cover: front */
.hero{position:absolute;left:500px;top:0;width:500px;height:500px;background:radial-gradient(circle at 62% 40%,#b4532a 0,#8a3a1c 28%,#3a1c12 48%,#141212 70%)}
.brand-band{position:absolute;left:740px;top:414px;width:260px;height:62px;background:var(--green)}
.brand{position:absolute;left:734px;top:424px;width:244px;height:44px;background:var(--black);color:var(--white);display:flex;align-items:center;gap:10px;padding-left:14px;font-size:19px}
.brand .dot{width:22px;height:22px;border-radius:50%;background:var(--green)}

/* price menu */
.price-table{position:absolute;top:23px;font-family:"Roboto Condensed","Arial Narrow",sans-serif;font-size:14.4px}
.left{left:22px;width:456px}
.right{left:522px;width:456px}
.head,.row,.section{display:grid;grid-template-columns:243px 54.5px 54.5px 54.5px 1fr;height:21.8px;align-items:center}
.head{background:var(--green);color:var(--white);font-weight:700;height:21px}
.head span{padding-left:5px}
.head span:first-child{padding:0}
.section{padding-left:5px;font-size:14.8px}
.section span:first-child{font-weight:700}
.section span + span{font-size:14.4px;padding-left:0;margin-left:-5px}
.section.divided{border-top:2px solid var(--green)}
.row span:first-child{padding-left:11px}
.foliage{position:absolute;left:320px;top:400px;width:200px;height:140px;background:radial-gradient(ellipse at 50% 60%,rgba(202,223,130,.35),rgba(202,223,130,0) 70%)}
.foliage-r{position:absolute;left:830px;top:350px;width:170px;height:180px;background:radial-gradient(ellipse at 50% 50%,rgba(202,223,130,.35),rgba(202,223,130,0) 70%)}
.notes{position:absolute;left:522px;top:397px;font-family:"Roboto Condensed","Arial Narrow",sans-serif;font-size:14px;line-height:18.5px}
.pricing{position:absolute;left:522px;top:457px;width:460px;text-align:center;font-family:"Roboto Condensed","Arial Narrow",sans-serif;font-size:14px;line-height:18.5px}
.sizes{margin-top:6px}
.sizes b{color:var(--green-text)}
.menu-bar{position:absolute;left:0;bottom:0;width:1000px;height:20px;background:var(--black)}
</style>
</head>
<body>

<section class="sheet cover">
  <p class="quote"><span class="mark">“</span>Living a more natural and organic life is a philosophy not just a product certification<span class="mark">”</span></p>
  <div class="quote-rule"></div>

  <div class="locations">
    <div class="location"><h3>KESTREL BAY</h3><p>Shop 1018 Kestrel Bay Plaza, Harbour Rd, Kestrel Bay</p><p>+ 61 (07) 3100 4821</p><p>kestrelbay@verdantroots.com.au</p></div>
    <div class="location"><h3>AMBERVALE</h3><p>Shop 231 Ambervale Central, Linden Road, Ambervale</p><p>+ 61 (07) 3100 4822</p><p>ambervale@verdantroots.com.au</p></div>
    <div class="location"><h3>MARLOW HEIGHTS</h3><p>Shop 3082 Marlow Heights Shopping Centre, Fenwick Rd Marlow Heights</p><p>+61 (07) 3100 4823</p><p>marlowheights@verdantroots.com.au</p></div>
    <div class="location"><h3>WILLOWMERE</h3><p>Shop 1255 Willowmere Square, Prospect St., Willowmere</p><p>+61 (07) 3100 4824</p><p>willowmere@verdantroots.com.au</p></div>
    <div class="location"><h3>RIVERSIDE WOMEN’S HOSPITAL</h3><p>Carrow St., Riverside QLD 4090</p><p>+61 (07) 3100 4825</p><p>rwh@verdantroots.com.au</p></div>
  </div>
  <div class="web-bar">WWW.VERDANTROOTS.COM.AU</div>

  <div class="hero" role="img" aria-label="Portrait photograph of a model with a glossy copper bob haircut on a dark background"></div>
  <div class="brand-band"></div>
  <div class="brand"><span class="dot"></span><span>Verdant Roots</span></div>
</section>

<section class="sheet menu">
  <div class="foliage" role="img" aria-label="Faint green leaf and vine flourish"></div>
  <div class="foliage-r" role="img" aria-label="Faint green leaf and vine flourish"></div>

  <div class="price-table left">
    <div class="head"><span></span><span>S</span><span>M</span><span>L</span><span>XL</span></div>
    <div class="section"><span>CUT &amp; BLOWDRY</span></div>
    <div class="row"><span style="font-size:15.5px">Ladies</span><span>$77</span><span>$88</span><span>$99</span><span>$110</span></div>
    <div class="section divided"><span>FRINGE</span></div>
    <div class="row"><span>Trim</span><span>$25</span></div>
    <div class="row"><span>Restyle</span><span>$35</span></div>
    <div class="section divided"><span>MENS</span></div>
    <div class="row"><span>Single Clipper</span><span>$28</span></div>
    <div class="row"><span>Style Cut</span><span>$42</span></div>
    <div class="section divided"><span>CHILDREN</span></div>
    <div class="row"><span>10 and under</span><span>$24</span></div>
    <div class="row"><span>11–16 Male</span><span>$32</span></div>
    <div class="row"><span>11–16 Female</span><span>$48</span></div>
    <div class="row"><span>Add a wash</span><span>$5</span></div>
    <div class="section divided"><span>BLOWDRY</span><span>$47</span><span>$57</span><span>$67</span><span>$77</span></div>
    <div class="row"><span>Shampoo and dry off</span><span>$25</span></div>
    <div class="section divided"><span>TREATMENTS</span></div>
    <div class="row"><span>Deep Treatment</span><span>$35</span></div>
    <div class="row"><span>Head Spa Ritual</span><span>$65</span></div>
    <div class="section divided"><span>UPSTYLE</span></div>
    <div class="row"><span>45 minutes</span><span>$85</span></div>
    <div class="row"><span>60 minutes</span><span>$120</span></div>
  </div>

  <div class="price-table right">
    <div class="head"><span></span><span>S</span><span>M</span><span>L</span><span>XL</span></div>
    <div class="section"><span>COLOUR</span></div>
    <div class="row"><span>Regrowth</span><span>$83</span></div>
    <div class="row"><span>Full Colour Tint</span><span>$125</span><span>$145</span><span>$165</span><span>$185</span></div>
    <div class="row"><span>Regrowth Lightenting*</span><span>$165</span><span>$189</span><span>$209</span><span>$229</span></div>
    <div class="row"><span>Balayage/Ombre*</span><span></span><span>$275</span><span>$375</span><span>$475</span></div>
    <div class="section divided"><span>LUMEA</span></div>
    <div class="row"><span>Regrowth</span><span>$99</span></div>
    <div class="row"><span>Full Colour Tint</span><span>$155</span><span>$175</span><span>$195</span><span>$205</span></div>
    <div class="section divided"><span>FOILS*</span></div>
    <div class="row"><span>Single*</span><span>$11</span><span>$13</span><span>$17</span><span>$22</span></div>
    <div class="row"><span>1/4 Head</span><span>$135</span><span>$155</span><span>$175</span><span>$195</span></div>
    <div class="row"><span>1/2 Head</span><span>$185</span><span>$205</span><span>$235</span><span>$265</span></div>
    <div class="row"><span>Full Head</span><span>$235</span><span>$265</span><span>$315</span><span>$355</span></div>
    <div class="section divided"><span>STRAIGHT</span></div>
    <div class="row"><span>Keratin Straightening System</span><span>$365</span><span>$445</span><span>$535</span><span>$565</span></div>
  </div>

  <div class="notes">
    <p>*Includes colour match and toner</p>
    <p>*Minimum 6 foils without colour</p>
    <p>*Minimum charge on a Sunday is $40</p>
  </div>
  <div class="pricing">
    <p>Pricing is indicative fo average products used and time taken for each service.</p>
    <p>You will ALWAYS receive a firm price after your consultation.</p>
    <p class="sizes"><b>S</b> to the jaw line &nbsp;<b>M</b> to the collarbone &nbsp;<b>L</b> to the bra strap &nbsp;<b>XL</b> past bra strap</p>
  </div>
  <div class="menu-bar"></div>
</section>

</body>
</html>
```